Dalvo Kin Business card Design

we need a business card design that is modern , easy to read , and remember able. the business sells all aspects of cooking and cooling equipment for restaurants, bars, cafe and large domestic kitchens
our website : www.dalvokingroup.com

Industry/Entity Type

Cooking

```html
<!DOCTYPE html>
<html lang="en">
<head>
<meta charset="utf-8">
<title>Dalvo Kin Business Card</title>
<link href="https://fonts.googleapis.com/css2?family=Baloo+Tamma+2:wght@700&display=swap" rel="stylesheet">
<style>
  :root {
    --cyan: #00e5ff;
    --white: #ffffff;
    --stage: #f4f6f7;
    --shadow: rgba(0, 0, 0, 0.12);
  }
  * { margin: 0; padding: 0; box-sizing: border-box; }
  html, body {
    width: 1200px;
    height: 704px;
    overflow: hidden;
    background: var(--stage);
  }
  .canvas {
    position: relative;
    width: 1200px;
    height: 704px;
    font-family: "Baloo Tamma 2", sans-serif;
    font-weight: 700;
  }
  .card {
    position: absolute;
    top: 171px;
    width: 532px;
    height: 312px;
    background: var(--cyan);
    border-radius: 2px;
    overflow: hidden;
    box-shadow: 0 6px 18px var(--shadow);
  }
  .card--front { left: 61px; }
  .card--back { left: 606px; }

  .brand {
    position: absolute;
    left: 0;
    width: 100%;
    text-align: center;
    color: var(--white);
    text-transform: uppercase;
    letter-spacing: 2px;
  }
  .card--front .brand { top: 96px; font-size: 22px; line-height: 30px; }
  .card--back .brand { top: 176px; font-size: 36px; line-height: 44px; letter-spacing: 4px; }

  .person {
    position: absolute;
    top: 153px;
    left: 0;
    width: 100%;
    text-align: center;
    color: var(--white);
    font-size: 16px;
    line-height: 24px;
  }

  .contact-band {
    position: absolute;
    left: 0;
    top: 0;
    width: 532px;
    height: 312px;
  }

  .contact {
    position: absolute;
    top: 242px;
    left: 0;
    width: 100%;
    text-align: center;
    color: var(--cyan);
    font-size: 16.5px;
    line-height: 22px;
  }
</style>
</head>
<body>
<main class="canvas">
  <section class="card card--front" aria-label="Business card front">
    <svg class="contact-band" viewBox="0 0 532 312" aria-hidden="true">
      <polygon points="0,259 265,215 532,259 532,312 0,312" fill="#ffffff"/>
    </svg>
    <p class="brand">Dalvo Kin</p>
    <div class="person">
      <p class="person__name">Mr.Abcdefg</p>
      <p class="person__title">Marketing Maneger</p>
    </div>
    <div class="contact">
      <p class="contact__address">Address : 27 Elm lane , Oak Park - Westford</p>
      <p class="contact__phone">Contact : 555014827</p>
      <p class="contact__web">Website : www.dalvokingroup.com</p>
    </div>
  </section>

  <section class="card card--back" aria-label="Business card back">
    <p class="brand">Dalvo Kin</p>
  </section>
</main>
</body>
</html>
```